Stationery including letterhead, business cards, for a new Chartered Accounting Practice

I need a new set of stationery including letterhead, business cards, for a new Chartered Accounting Practice based in Melbourne, Victoria, Australia called "Brody Kettleworth, Chartered Accountant".

I will be providing Auditing and general consulting advice to small and medium business enterprises. The final design should communicate trust, wisdom and security.

Target Market(s)

Target Market English speaking, Australians. Proprietors small and medium sized businesses - aged 45-65. Fellow professionals - lawyers, investment consultants, other accountants. Retirees - aged 60 and over

Industry/Entity Type

Accountant

Font styles to use
Serif

Colors
0355a3

Requirements
Must have
• The final design should convey trust, wisdom and security.
• Names of practice "Brody Kettleworth , Chartered Accountant"
• Contact details:
• Address 214 Carrowdale Street, Fennick Vale, Victoria, 3058, Australia
• Telephone: 047 000 3815
• Email: brodykettleworth@mailbarrow.net
Nice to have
• an expensive and professional design, the letterhead should be timeless with a logo on white space
Should not have
• no bright/fluro colours

```html
<!DOCTYPE html>
<html lang="en">
<head>
<meta charset="utf-8">
<title>Brody Kettleworth, Chartered Accountant – Business Cards</title>
<link rel="stylesheet" href="https://fonts.googleapis.com/css2?family=Cinzel:wght@500&family=Open+Sans:wght@400&display=swap">
<style>
  :root {
    --brand-blue: #0355a3;
    --paper: #ffffff;
    --stripe-grey: #8a8a8a;
    --ink: #3a3a3a;
    --backdrop: #ecebe8;
  }
  * { box-sizing: border-box; margin: 0; padding: 0; }
  html, body {
    width: 1200px; height: 900px; overflow: hidden;
    background: var(--backdrop);
  }
  .sheet {
    position: relative; width: 1200px; height: 900px;
    display: flex; align-items: center; justify-content: center; gap: 40px;
  }
  .card {
    position: relative; width: 540px; height: 327px; overflow: hidden;
    box-shadow: 0 6px 18px rgba(0,0,0,0.18);
  }
  .card--front {
    background: var(--brand-blue);
    display: flex; align-items: center; justify-content: center;
  }
  .card--back { background: var(--paper); }

  .wordmark { text-align: center; }
  .wordmark__row { display: flex; align-items: center; justify-content: center; gap: 12px; }
  .wordmark__dot { width: 14px; height: 14px; border-radius: 50%; background: currentColor; }
  .wordmark__name {
    font-family: "Cinzel", serif; font-weight: 500;
    font-size: 34px; letter-spacing: 0.5px; line-height: 1;
  }
  .wordmark__title {
    font-family: "Open Sans", sans-serif; font-size: 12px;
    letter-spacing: 5.4px; margin-top: 6px;
  }
  .card--front .wordmark { color: var(--paper); }

  .card--back .wordmark {
    position: absolute; top: 46px; right: 28px; color: var(--brand-blue);
  }
  .card--back .wordmark__name { font-size: 25px; }
  .card--back .wordmark__dot { width: 10px; height: 10px; }
  .card--back .wordmark__title { font-size: 9px; letter-spacing: 3.9px; color: var(--ink); margin-top: 4px; }

  .wave { position: absolute; inset: 0; width: 540px; height: 327px; }
  .wave__band { fill: var(--brand-blue); }
  .wave__stripe { fill: var(--stripe-grey); }

  .contact {
    position: absolute; left: 30px; top: 140px;
    font-family: "Open Sans", sans-serif; color: var(--ink);
  }
  .contact__line { display: flex; align-items: center; gap: 7px; font-size: 14px; line-height: 21px; }
  .contact__icon { width: 12px; height: 12px; fill: var(--brand-blue); }
  .contact__address { font-size: 15px; line-height: 21px; margin-top: 18px; font-style: normal; }
</style>
</head>
<body>
<main class="sheet">
  <section class="card card--front" aria-label="Business card front">
    <div class="wordmark">
      <div class="wordmark__row">
        <span class="wordmark__dot"></span>
        <span class="wordmark__name">Brody Kettleworth</span>
      </div>
      <div class="wordmark__title">CHARTERED ACCOUNTANT</div>
    </div>
  </section>

  <section class="card card--back" aria-label="Business card back">
    <svg class="wave" viewBox="0 0 540 327" aria-hidden="true">
      <path class="wave__stripe" d="M0 288 C200 300 380 250 470 180 C400 250 200 312 0 314 Z"/>
      <path class="wave__band" d="M0 318 C210 322 400 262 540 170 L540 327 L0 327 Z"/>
    </svg>

    <div class="wordmark">
      <div class="wordmark__row">
        <span class="wordmark__dot"></span>
        <span class="wordmark__name">Brody Kettleworth</span>
      </div>
      <div class="wordmark__title">CHARTERED ACCOUNTANT</div>
    </div>

    <div class="contact">
      <div class="contact__line">
        <svg class="contact__icon" viewBox="0 0 24 24"><path d="M6.6 10.8a15 15 0 0 0 6.6 6.6l2.2-2.2a1 1 0 0 1 1-.25 11.4 11.4 0 0 0 3.6.57 1 1 0 0 1 1 1V20a1 1 0 0 1-1 1A17 17 0 0 1 3 4a1 1 0 0 1 1-1h3.5a1 1 0 0 1 1 1c0 1.25.2 2.45.57 3.57a1 1 0 0 1-.25 1z"/></svg>
        <span>047 000 3815</span>
      </div>
      <div class="contact__line">
        <svg class="contact__icon" viewBox="0 0 24 24"><path d="M2 5h20v14H2z M2 5l10 8 10-8" fill="var(--brand-blue)" stroke="#fff" stroke-width="1.6"/></svg>
        <span>brodykettleworth@mailbarrow.net</span>
      </div>
      <address class="contact__address">
        214 Carrowdale Street,<br>
        Fennick Vale, Victoria, 3058, Australia
      </address>
    </div>
  </section>
</main>
</body>
</html>
```